Re-design my 1-page website to be BETTER!

Hi Guys,
I recently created a 1-page website for market testing purposes for a company I am starting. Problem is, the feedback i've had on the page is its a bit corporate and boring.
I would love you to design something that is fresher, more modern and will generate leads (via the sign up CTA's).
Here is the website as it is now: www.guidebridgehub.com.au.
If you need any info or have questions, just reach out.
Thanks,
Oliver

Target Market(s)

Entrepreneurs

Number of Pages Required

1 page

Font styles to use
Sans Serif

Colors
abd036
34a6d7
ffffff

Requirements
Must have
• Fresh, Modern, high-converting
• I expect 70% of traffic to be mobile so must be mobile optimised first.
Nice to have
• I've highlighted colours i like below, however, I am open to suggestions. I like colours that are gender neutral and show energy and vibrancy.
• I have used Proxima Nova for the fonts, as I find it easy to read however, I am open to suggestions. My main preference is that it displays well and is easily read

```html
<!DOCTYPE html>
<html lang="en">
<head>
<meta charset="utf-8">
<title>GuideBridge — A Mentor for Everyone</title>
<link href="https://fonts.googleapis.com/css2?family=DM+Sans:wght@400;500;700&family=Montserrat:wght@400;500&display=swap" rel="stylesheet">
<style>
:root{
  --navy:#0e1b55;
  --green:#1dd100;
  --grey-text:#8b8d94;
  --note:#a7a9b0;
  --mist:#e9eaf0;
  --white:#ffffff;
}
*{margin:0;padding:0;box-sizing:border-box}
html,body{width:1200px;height:5216px;overflow:hidden;background:var(--white)}
body{font-family:"Montserrat",sans-serif;color:var(--grey-text);position:relative}
.section{position:absolute;left:0;width:1200px;overflow:hidden}
.accent{color:var(--green)}
.btn{position:absolute;display:flex;align-items:center;justify-content:center;background:var(--green);color:var(--white);border-radius:24px;font:500 14px "Montserrat",sans-serif;text-decoration:none}
.note{position:absolute;font-size:11.5px;color:var(--note);white-space:nowrap}
.heading{font-family:"DM Sans",sans-serif;font-weight:700;color:var(--navy);letter-spacing:-2.5px;white-space:nowrap}
.photo{position:absolute}

/* hero */
.hero{top:0;height:749px}
.hero .photo{inset:0;background:linear-gradient(115deg,#4a6aae 0%,#7391c6 40%,#a7badb 62%,#6c87bf 80%,#4d69ab 100%)}
.hero .shade{position:absolute;inset:0;background:linear-gradient(90deg,rgba(38,66,146,.55),rgba(38,66,146,.12))}
.brand{position:absolute;left:84px;top:22px;font:500 29px "DM Sans",sans-serif;color:var(--white);letter-spacing:-.5px}
.menu{position:absolute;left:1130px;top:33px}
.hero h1{position:absolute;left:123px;top:232px;font:500 77px "Montserrat",sans-serif;color:var(--white);letter-spacing:-1px;white-space:nowrap}
.hero .lede{position:absolute;left:125px;top:338px;width:505px;font-size:16.5px;line-height:29px;color:var(--white)}
.hero .note{color:rgba(255,255,255,.6)}

/* intro */
.intro{top:749px;height:749px}
.intro h2{position:absolute;left:125px;top:148px;font-size:30px;letter-spacing:-1.3px}
.intro .copy{position:absolute;left:125px;top:202px;width:460px;font-size:13.5px;line-height:23.5px}
.intro .copy p{margin-bottom:23px}
.intro .photo{left:680px;top:100px;width:420px;height:649px;background:linear-gradient(180deg,#e8d8cc 0%,#b98466 22%,#27334a 48%,#2b3750 100%);border-radius:160px 160px 0 0}

/* different */
.different{top:1498px;height:749px;background:var(--mist)}
.different h2{position:absolute;left:0;width:1200px;text-align:center;top:88px;font-size:61px}
.different .sub{position:absolute;left:0;width:1200px;text-align:center;top:180px;font-size:16.5px;line-height:29px}
.step{position:absolute;top:300px;width:270px}
.step h3{font:700 19px "DM Sans",sans-serif;color:var(--navy);letter-spacing:-.6px;margin-bottom:12px}
.step p{font-size:13px;line-height:23.5px}

/* growth */
.growth{top:2247px;height:981px}
.growth h2{position:absolute;left:0;width:1200px;text-align:center;top:140px;font-size:62px;line-height:74px}
.benefit{position:absolute;width:395px}
.benefit h3{font:700 19px "DM Sans",sans-serif;color:var(--navy);letter-spacing:-.6px;margin-bottom:8px}
.benefit p{font-size:13px;line-height:23px}

/* reimagined */
.reimagined{top:3228px;height:389px}
.reimagined .photo{inset:0;background:linear-gradient(180deg,#3e63a8 0%,#6f8fc4 38%,#4d6290 62%,#7a716e 100%)}
.reimagined h2{position:absolute;left:0;width:1200px;text-align:center;top:82px;font-size:62px;color:var(--white)}
.reimagined .sub{position:absolute;left:0;width:1200px;text-align:center;top:180px;font-size:16.5px;line-height:28px;color:var(--white)}

/* faq */
.faq{top:3617px;height:846px;background:var(--mist)}
.faq h2{position:absolute;left:0;width:1200px;text-align:center;top:98px;font-size:31px;letter-spacing:-1.3px}
.q{position:absolute;left:232px;font:700 17px "DM Sans",sans-serif;color:var(--green);letter-spacing:-.4px;display:flex;align-items:center;gap:16px;white-space:nowrap}
.q svg{display:block}
.answer{position:absolute;left:232px;width:730px;font-size:13px;line-height:23.5px}

/* invest */
.invest{top:4463px;height:753px}
.invest .photo{inset:0;background:linear-gradient(160deg,#2f5a3a 0%,#4a6fa8 30%,#3e5ea6 65%,#6d87bd 100%)}
.invest h2{position:absolute;left:0;width:1200px;text-align:center;top:150px;font-size:62px;color:var(--white)}
.invest .sub{position:absolute;left:0;width:1200px;text-align:center;top:240px;font-size:16.5px;line-height:29px;color:var(--white)}
.field{position:absolute;top:435px;height:45px;background:rgba(255,255,255,.2);color:var(--white);font-size:14px;display:flex;align-items:center;padding-left:16px}
.invest .note{color:rgba(255,255,255,.55)}
</style>
</head>
<body>

<header class="section hero">
  <div class="photo" role="img" aria-label="Photo of a mentor and mentee talking over a tablet and coffee"></div>
  <div class="shade"></div>
  <div class="brand">GuideBridge</div>
  <svg class="menu" width="24" height="18" viewBox="0 0 24 18"><rect y="1" width="24" height="2.4" fill="#fff"/><rect y="8" width="24" height="2.4" fill="#fff"/><rect y="15" width="24" height="2.4" fill="#fff"/></svg>
  <h1>A Mentor for <span class="accent">Everyone</span></h1>
  <p class="lede">“We’ve flipped the model on its head - &nbsp;so now you choose your Mentor. &nbsp;It’s never been this easy to get the advice and guidance you need to thrive”</p>
  <a class="btn" style="left:125px;top:457px;width:191px;height:45px">Find my mentor</a>
  <p class="note" style="left:125px;top:525px">Free Registration. 100% Confidential. 100% Obligation Free</p>
</header>

<section class="section intro">
  <h2 class="heading">Finding a Mentor Has Never Been Easier</h2>
  <div class="copy">
    <p>Having a great Mentor will turbo-charge your personal, professional or business growth. &nbsp;But unless you have an incredible network, finding great Mentors has always been a challenge.</p>
    <p>GuideBridge changes all that, levelling the playing field and making it easy for entrepreneurs and professionals to find the advice and guidance they deserve.</p>
    <p>No longer will you have to go searching for your perfect Mentor. We bring the perfect Mentor to you, selected from a global pool of experts, putting the power back in your hands and letting you get on with your growth.</p>
  </div>
  <a class="btn" style="left:125px;top:542px;width:191px;height:48px">Find my mentor</a>
  <p class="note" style="left:125px;top:603px">Register Free. 100% confidential. Obligation Free</p>
  <div class="photo" role="img" aria-label="Photo of a smiling young woman with curly hair in a floral dress"></div>
</section>

<section class="section different">
  <h2 class="heading">Mentorship: <span class="accent">But Different</span></h2>
  <p class="sub">Finding a Mentor used to be hard; but not any more.<br>We’ve turned the traditional model on its head, so <span class="accent">now Mentors seek you.</span></p>
  <div class="step" style="left:142px">
    <h3>Tell Us What You Need</h3>
    <p>There is no one size fits all approach to Mentorship. &nbsp;So tell us the challenges you are facing and the skill-set your Mentor must have.</p>
  </div>
  <div class="step" style="left:467px">
    <h3>Choose Your Mentor</h3>
    <p>Mentors are invited to Mentor you. We select 3 top picks that align with your criteria. &nbsp;It’s then up to you whether you choose a Mentor, interview 1 or more or refine your criteria and start again.</p>
  </div>
  <div class="step" style="left:791px">
    <h3>Ongoing Support</h3>
    <p>We don’t stop once you have your perfect Mentor. &nbsp;We’re on hand to make life easy for you, keep your sessions on track and provide ongoing support.</p>
  </div>
  <a class="btn" style="left:504px;top:540px;width:191px;height:47px">Register for free</a>
  <p class="note" style="left:0;width:1200px;text-align:center;top:604px">Register Free. 100% confidential. Obligation Free</p>
</section>

<section class="section growth">
  <h2 class="heading">How a Mentor Will<br>Accelerate <span class="accent">Your Growth</span></h2>
  <div class="benefit" style="left:138px;top:380px">
    <h3>1. Impartial advice</h3>
    <p>Imagine being able to speak to someone who has been through the challenges you are currently facing? &nbsp;Who has “been there seen that” and can help you navigate the ups and downs of your career or business?</p>
  </div>
  <div class="benefit" style="left:140px;top:530px">
    <h3>2. Avoid the Pitfalls</h3>
    <p>An experienced Mentor will help you see the challenges before they arise and make sure you avoid them altogether. &nbsp;Saving valuable time and money in the process.</p>
  </div>
  <div class="benefit" style="left:138px;top:680px">
    <h3>3. A Supportive Ear</h3>
    <p>Running a business and the challenges of corporate life can be extremely stressful. &nbsp;And often, our friends and family just don’t get it. &nbsp;So imagine having someone independent who can understand where your coming from and, help you see things objectively.</p>
  </div>
  <div class="benefit" style="left:627px;top:380px">
    <h3>4. Clarity</h3>
    <p>Sometimes we are so caught up in our own world we struggle to see the big picture. &nbsp;You Mentor will provide an objective, outsider view. &nbsp;Helping you to cut though the noise and focus on what’s really important.</p>
  </div>
  <div class="benefit" style="left:627px;top:530px">
    <h3>5. Motivation</h3>
    <p>Your Mentor has seen this before and been in your shoes. They understand what your going through and will help you to re-focus and re-energise.</p>
  </div>
  <div class="benefit" style="left:627px;top:680px">
    <h3>6. Make you Accountable</h3>
    <p>A Mentor is not just there to pick you up - they are to give honest appraisal and tell you when your falling short. Ultimately, only you can control your success and you Mentor will hold you accountable to make sure you are.</p>
  </div>
</section>

<section class="section reimagined">
  <div class="photo" role="img" aria-label="Photo of a person with raised arms on a mountain top above a blue valley"></div>
  <h2 class="heading">Mentorship <span class="accent">reimagined</span></h2>
  <p class="sub">You are closer to your perfect mentor than you think.<br>Register today to see how easy it can be.</p>
  <a class="btn" style="left:504px;top:259px;width:191px;height:49px">Register now</a>
</section>

<section class="section faq">
  <h2 class="heading">Frequently Asked Questions</h2>
  <div class="q" style="top:207px">What is a Mentor? <svg width="9" height="12" viewBox="0 0 9 12"><path d="M0 0L9 6L0 12Z" fill="#1dd100"/></svg></div>
  <p class="answer" style="top:246px">Experienced and Trusted Advisor. Guru. Confidente. Friend.</p>
  <p class="answer" style="top:292px">In essence a Mentor is someone who can turn to for guidance and advice. Someone who is more experienced than you and, has navigated similar challenges to you and can foresee the pitfalls and hurdles you face.</p>
  <p class="answer" style="top:384px">A great Mentor is also a motivator, connector and guide. &nbsp;Will help you focus on what’s really important and see the bigger picture. Importantly, a great Mentor should be outside your immediate network of friends and relatives. &nbsp;And, be able to offer unbiased, honest and objective advice, that you can action.</p>
  <div class="q" style="top:473px">Is a Mentor right for me? <svg width="9" height="12" viewBox="0 0 9 12"><path d="M0 0L9 6L0 12Z" fill="#1dd100"/></svg></div>
  <div class="q" style="top:515px">How often do we meet? <svg width="9" height="12" viewBox="0 0 9 12"><path d="M0 0L9 6L0 12Z" fill="#1dd100"/></svg></div>
  <div class="q" style="top:558px">Can I have more than one mentor? <svg width="9" height="12" viewBox="0 0 9 12"><path d="M0 0L9 6L0 12Z" fill="#1dd100"/></svg></div>
  <div class="q" style="top:600px">What if it doesn’t work out? <svg width="9" height="12" viewBox="0 0 9 12"><path d="M0 0L9 6L0 12Z" fill="#1dd100"/></svg></div>
  <div class="q" style="top:643px">How do we meet? <svg width="9" height="12" viewBox="0 0 9 12"><path d="M0 0L9 6L0 12Z" fill="#1dd100"/></svg></div>
  <div class="q" style="top:683px">What are the costs? <svg width="9" height="12" viewBox="0 0 9 12"><path d="M0 0L9 6L0 12Z" fill="#1dd100"/></svg></div>
</section>

<section class="section invest">
  <div class="photo" role="img" aria-label="Photo of a smiling woman holding a phone outdoors among trees"></div>
  <h2 class="heading">It’s time to <span class="accent">invest in you</span></h2>
  <p class="sub">If you’ve come this far you’ve already taken the most important<br>step: recognising how mentorship can help you; and taking action<br>to find it. And now your here, the rest is easy.</p>
  <p class="sub" style="top:352px">Get started now and let GuideBridge do the rest…</p>
  <div class="field" style="left:314px;width:277px">Your Name</div>
  <div class="field" style="left:607px;width:278px">E-Mail</div>
  <a class="btn" style="left:506px;top:522px;width:190px;height:47px">Let’s do this</a>
  <p class="note" style="left:0;width:1200px;text-align:center;top:585px">Sign up is free, obligation free and 100% confidential</p>
</section>

</body>
</html>
```